Door Hanger Design for Electricians Serving Homes

I would like our logo incorporated into the door hanger. We would like a place for a tear off section on the bottom of the hanger with our contact information: K&T Electric - (555) 318-4076 - www.kandtelectricqz.com - info@kandtelectricqz.com.
Door Hanger Script
Front Side of the Door Hanger:
[Company Logo]
Need a Reliable Electrician?
Your Local Electrical Expert is Just Around the Corner!
• Quick Response Times
• Affordable Rates
• Quality Workmanship
• Fully Licensed & Insured
• Special Offer:
• 10% OFF Your First Service Call!
Back Side of the Door Hanger:
Don't Let Electrical Issues Keep You in the Dark!
From flickering lights to complete system upgrades, we've got all your
residential electrical needs covered. Our services include:
• Electrical Repairs & Troubleshooting
• Lighting Installation & Upgrades
• Safety Inspections & Code Compliance
• Energy-Efficient Solutions
• 24/7 Emergency Services
• Why Choose Us?
• Friendly, Local Service
• Over 30 Years of Experience
• Satisfaction Guaranteed
• Upfront Pricing
Call Us Today: [Your Phone Number]
Visit Our Website: [Your Website]
Book Your Appointment Now and Claim Your 10% Discount!
Offer valid for new customers on the first visit only. Mention this door hanger when
booking.
[Your Company Name and Contact Information]
Follow Us on Social Media for More Tips and Special Offers!
[Icons for social media platforms: Plumnest, Glimmorow, Quibbly, etc.]
Design Tips:
Use bold, clear fonts for easy reading.
Incorporate your brand colors and logo for instant recognition.
Include a clear call to action (CTA) on both sides.
Add a tear-off section at the bottom with your contact information for
convenience.
Use high-quality images or graphics related to electrical work to catch
the eye.
This door hanger design and copy aim to attract residential clients by
highlighting the benefits of your electrical services, special offers, and
how they can easily get in touch with you for their electrical needs.
The door knocker template will have three of the same design on front and three of the same design on the back. This template is from the print shop.

```html
<!DOCTYPE html>
<html lang="en">
<head>
<meta charset="utf-8">
<title>K&amp;T Electric Door Hanger</title>
<link rel="stylesheet" href="https://fonts.googleapis.com/css2?family=EB+Garamond:wght@600;700&family=Figtree:wght@400;500&family=Archivo:wght@800&family=Roboto+Condensed:wght@700&display=swap">
<style>
  :root {
    --red: #b00006;
    --bright-red: #c8101a;
    --ink: #111111;
    --paper: #fafafa;
    --white: #ffffff;
    --photo-top: #8091b0;
    --photo-bottom: #4f5c80;
    --label: #5a5a5a;
  }
  * { margin: 0; padding: 0; box-sizing: border-box; }
  html, body { width: 1200px; height: 1066px; overflow: hidden; background: var(--white); }
  body { position: relative; font-family: "Figtree", sans-serif; }
  .serif { font-family: "EB Garamond", serif; font-weight: 700; }

  .hanger {
    position: absolute;
    width: 392px; height: 909px;
    background: var(--paper);
    overflow: hidden;
    box-shadow: -10px 12px 28px rgba(0,0,0,0.28);
  }
  .hanger--front { left: 158px; top: 73px; }
  .hanger--back  { left: 689px; top: 68px; }
  .hanger > * { position: absolute; }
  .backdrop { left: 0; top: 0; width: 392px; height: 909px; }

  .side-label {
    position: absolute; font-size: 24px; color: var(--label);
    letter-spacing: 0.5px; transform: translateX(-50%);
  }

  /* front */
  .hero-title {
    left: 0; width: 392px; top: 183px; text-align: center;
    color: var(--white); font-size: 31px; line-height: 35px; font-weight: 600;
    font-family: "EB Garamond", serif;
  }
  .front-question {
    left: 0; width: 392px; top: 393px; text-align: center;
    color: var(--red); font-size: 28px;
  }
  .benefits { left: 44px; top: 440px; list-style: none; }
  .benefits li {
    display: flex; align-items: center; gap: 12px;
    font-size: 24px; color: var(--ink); height: 43px;
  }
  .benefits svg { width: 18px; height: 30px; fill: var(--bright-red); }

  .offer { left: 24px; top: 636px; }
  .offer-amount {
    font-family: "Archivo", sans-serif; font-weight: 800;
    font-size: 66px; line-height: 64px; color: var(--ink); letter-spacing: -2px;
  }
  .offer-off {
    font-family: "Roboto Condensed", sans-serif; font-size: 18px;
    color: var(--bright-red); letter-spacing: 0; margin-left: 4px;
  }
  .offer-note {
    font-family: "Roboto Condensed", sans-serif; font-size: 18px;
    color: var(--bright-red); margin-top: 2px;
  }

  .brand {
    display: flex; align-items: center; gap: 8px;
    font-family: "EB Garamond", serif; font-weight: 700; color: var(--ink);
    white-space: nowrap;
  }
  .brand-dot { border-radius: 50%; background: var(--bright-red); flex: none; }
  .hanger--front .brand { left: 212px; top: 668px; font-size: 24px; }
  .hanger--front .brand-dot { width: 14px; height: 14px; }
  .hanger--back .brand { left: 252px; top: 44px; font-size: 20px; }
  .hanger--back .brand-dot { width: 12px; height: 12px; }

  .front-tagline {
    left: 0; width: 392px; top: 791px; text-align: center;
    color: var(--white); font-size: 28px; line-height: 32px;
  }

  /* back */
  .back-title {
    left: 0; width: 393px; top: 180px; text-align: center;
    color: var(--ink); font-size: 30px; line-height: 35px;
  }
  .section-title { left: 37px; color: var(--white); font-size: 30px; line-height: 34px; }
  .section-title--services { top: 312px; }
  .section-title--why { top: 485px; }
  .checklist { left: 37px; list-style: none; }
  .checklist--services { top: 359px; }
  .checklist--why { top: 531px; }
  .checklist li {
    display: flex; align-items: center; gap: 10px;
    font-size: 16px; color: var(--white); height: 23.8px;
  }
  .checklist svg { width: 12px; height: 20px; fill: var(--white); }

  .cta {
    left: 35px; top: 638px; color: var(--white);
    font-size: 23px; line-height: 30px; font-weight: 600;
    font-family: "EB Garamond", serif;
  }
  .cta-terms { left: 35px; top: 706px; color: var(--white); font-size: 14px; line-height: 18px; }

  .contact { left: 0; width: 393px; top: 782px; text-align: center; color: var(--ink); }
  .contact-phone { font-family: "EB Garamond", serif; font-weight: 700; font-size: 42px; line-height: 44px; }
  .contact-line { font-family: "EB Garamond", serif; font-weight: 600; font-size: 16px; line-height: 18px; }

  .social { left: 112px; top: 867px; display: flex; gap: 15px; list-style: none; }
  .social li {
    width: 32px; height: 32px; border-radius: 50%; background: var(--ink);
    display: flex; align-items: center; justify-content: center; gap: 3px;
  }
  .social .more span { width: 5px; height: 5px; border-radius: 50%; background: var(--white); }
</style>
</head>
<body>

<svg width="0" height="0" style="position:absolute" aria-hidden="true">
  <defs>
    <symbol id="bolt" viewBox="0 0 12 20">
      <path d="M7 0 L1 11 H5 L3 20 L11 7 H7 L10 0 Z"/>
    </symbol>
  </defs>
</svg>

<!-- Front side -->
<section class="hanger hanger--front">
  <svg class="backdrop" viewBox="0 0 392 909">
    <defs>
      <linearGradient id="photoTone" x1="0" y1="0" x2="0" y2="1">
        <stop offset="0" stop-color="var(--photo-top)"/>
        <stop offset="1" stop-color="var(--photo-bottom)"/>
      </linearGradient>
    </defs>
    <path role="img" aria-label="Photo of an electrician in a hard hat working on a bundle of wires"
      d="M0 0 H392 V337 C350 352 310 362 270 370 C252 374 248 362 255 350 C258 338 240 336 220 342 C180 356 140 372 100 368 C60 364 30 348 0 332 Z"
      fill="url(#photoTone)"/>
    <line x1="80" y1="0" x2="166" y2="73" stroke="var(--white)" stroke-width="1.5" stroke-dasharray="10 8"/>
    <circle cx="194" cy="120" r="53" fill="none" stroke="var(--white)" stroke-width="1.5" stroke-dasharray="10 8"/>
    <path d="M0 787 C50 770 90 758 120 762 C132 764 128 782 145 784 C200 760 240 760 280 760 C330 762 365 780 392 793 V909 H0 Z"
      fill="var(--red)"/>
  </svg>

  <h1 class="hero-title">Your Local<br>Electrical Expert is<br>Just Around the Corner</h1>

  <h2 class="front-question serif">Need a Reliable Electrician?</h2>

  <ul class="benefits">
    <li><svg><use href="#bolt"/></svg>Quick Response Times</li>
    <li><svg><use href="#bolt"/></svg>Quality Workmanship</li>
    <li><svg><use href="#bolt"/></svg>Affordable Rates</li>
    <li><svg><use href="#bolt"/></svg>Fully Licensed &amp; Insured</li>
  </ul>

  <div class="offer">
    <div class="offer-amount">10%<span class="offer-off">OFF</span></div>
    <div class="offer-note">On First Service Call</div>
  </div>

  <div class="brand"><span class="brand-dot"></span>K&amp;T Electric</div>

  <p class="front-tagline serif">From flickering lights to<br>complete system upgrades,<br>we've got all your</p>
</section>

<!-- Back side -->
<section class="hanger hanger--back">
  <svg class="backdrop" viewBox="0 0 393 909">
    <line x1="78" y1="0" x2="165" y2="73" stroke="var(--red)" stroke-width="1.5"/>
    <circle cx="195" cy="120" r="53" fill="none" stroke="var(--red)" stroke-width="1.5"/>
    <path d="M0 259 C40 280 90 306 150 303 C200 300 230 270 255 272 C270 274 262 292 270 306 C300 302 350 278 393 259 V801 C350 778 300 760 250 760 C200 760 160 782 140 782 C125 780 130 762 110 760 C70 764 30 782 0 791 Z"
      fill="var(--red)"/>
  </svg>

  <div class="brand"><span class="brand-dot"></span>K&amp;T Electric</div>

  <h1 class="back-title serif">Don't Let Electrical<br>Issues Keep You in the Dark!</h1>

  <h2 class="section-title section-title--services serif">Our services</h2>
  <ul class="checklist checklist--services">
    <li><svg><use href="#bolt"/></svg>Electrical Repairs &amp; Troubleshooting</li>
    <li><svg><use href="#bolt"/></svg>Lighting Installation &amp; Upgrades</li>
    <li><svg><use href="#bolt"/></svg>Safety Inspections &amp; Code Compliance</li>
    <li><svg><use href="#bolt"/></svg>Energy-Efficient Solutions</li>
    <li><svg><use href="#bolt"/></svg>24/7 Emergency Services</li>
  </ul>

  <h2 class="section-title section-title--why serif">Why Choose Us?</h2>
  <ul class="checklist checklist--why">
    <li><svg><use href="#bolt"/></svg>Friendly, Local Service</li>
    <li><svg><use href="#bolt"/></svg>Over 30 Years of Experience</li>
    <li><svg><use href="#bolt"/></svg>Satisfaction Guaranteed</li>
    <li><svg><use href="#bolt"/></svg>Upfront Pricing</li>
  </ul>

  <p class="cta">Book Your Appointment Now and<br>Claim Your 10% Discount!</p>
  <p class="cta-terms">Offer valid for new customers on the first visit only.<br>Mention this door hanger when booking.</p>

  <div class="contact">
    <div class="contact-phone">555-318-4076</div>
    <div class="contact-line">www.kandtelectricqz.com</div>
    <div class="contact-line">info@kandtelectricqz.com</div>
  </div>

  <ul class="social">
    <li aria-label="Plumnest"></li>
    <li aria-label="Glimmorow"></li>
    <li aria-label="Quibbly"></li>
    <li class="more" aria-label="More"><span></span><span></span><span></span></li>
  </ul>
</section>

<p class="side-label" style="left:339px; top:1016px;">Front</p>
<p class="side-label" style="left:885px; top:1010px;">Back</p>

</body>
</html>
```